PowerPoint template for a tech startup

We need a PowerPoint template with a title slide, text slide, section slide, and thank you slide.
Our application helps engineering teams to be more productive. We would love a design that is slick, sophisticated, and consistent with our brand. (see more at www.quenvomi.io or attached files)
By the way (not a requirement), Quenvo means lighthouse in Greek.
Also, here is the font we used (not required) - https://fonts.trelvanic.com/fonts/league-gothic

Other font styles liked:
• https://fonts.trelvanic.com/fonts/league-gothic

```html
<!DOCTYPE html>
<html lang="en">
<head>
<meta charset="utf-8">
<title>Quenvo – Presentation Template</title>
<link href="https://fonts.googleapis.com/css2?family=League+Gothic&family=Oswald:wght@300;400;500&display=swap" rel="stylesheet">
<style>
  :root{
    --orange:#e8521e;
    --navy:#1b4f7a;
    --ink:#080808;
    --paper:#ffffff;
    --stage:#e9e9ea;
    --panel-dark:#1c1c1c;
  }
  *{margin:0;padding:0;box-sizing:border-box}
  html,body{width:1200px;height:519px;overflow:hidden;background:var(--stage)}
  .deck{position:relative;width:1200px;height:519px}
  .slide{position:absolute;width:356px;height:200px;overflow:hidden;box-shadow:0 3px 8px rgba(0,0,0,.28)}
  .s1{left:40px;top:45px}
  .s2{left:422px;top:45px;background:var(--paper)}
  .s3{left:804px;top:45px;background:var(--ink)}
  .s4{left:40px;top:274px;background:#f7f9fb}
  .s5{left:422px;top:274px;background:var(--ink)}
  .s6{left:804px;top:274px}
  .display{font-family:"League Gothic",Impact,sans-serif;font-weight:400;line-height:1;text-transform:uppercase}
  .body{font-family:Oswald,"Arial Narrow",sans-serif;font-weight:300}
  .abs{position:absolute}

  /* title slide */
  .hero-photo{position:absolute;inset:0;background:linear-gradient(180deg,#3e4a5a 0%,#8a8e94 30%,#c9a06c 55%,#5a5048 75%,#2a2e34 100%)}
  .hero-fade{position:absolute;inset:0;background:linear-gradient(90deg,rgba(255,255,255,0) 45%,rgba(235,236,238,.85) 72%,rgba(235,236,238,.9) 100%)}
  .wordmark{position:absolute;right:16px;top:12px;font-size:38px;color:var(--navy);letter-spacing:1px}
  .wordmark-rule{position:absolute;right:16px;top:50px;width:64px;height:1.2px;background:var(--navy)}
  .hero-get{left:196px;top:86px;font-size:24px;color:var(--orange)}
  .hero-get small{font-size:15px;color:var(--navy)}
  .hero-rule{left:196px;top:112px;width:160px;height:1px;background:var(--navy)}
  .hero-line{left:196px;font-size:20px;color:var(--navy)}
  .pill{left:196px;top:162px;width:132px;height:15px;border-radius:8px;background:var(--orange);color:#fff;font-family:"League Gothic",sans-serif;font-size:11.5px;line-height:15px;text-align:center}

  /* shared footer */
  .foot-num{left:7px;top:183px;font-family:"League Gothic",sans-serif;font-size:8px;line-height:8px}
  .foot-url{left:19px;top:184px;font-family:Oswald,sans-serif;font-size:4px;line-height:5px;letter-spacing:1.6px}
  .foot-rule{left:7px;right:0;top:192px;height:.8px;background:var(--orange)}
  .on-light{color:var(--navy)}
  .on-dark{color:#fff}

  /* text slides */
  .rule-navy{height:.8px;background:var(--navy)}
  .rule-orange{height:.8px;background:var(--orange)}
  .col-head{font-family:"League Gothic",sans-serif;font-size:10px;line-height:1.1}
  .col-text{font-size:3px;line-height:1.6;color:#555;text-align:justify}
  .col-text p{margin-bottom:7px}
  .dark-text{color:#e8e8e8}

  .feature-art{position:absolute;top:48px;width:72px;height:68px;background:linear-gradient(180deg,#222,#141414);border:.5px solid #333}
  .caption{font-family:"League Gothic",sans-serif;font-size:6px;color:#fff;line-height:1.15}
  .caption-sub{font-size:2.3px;color:#cfcfcf;line-height:1.4}

  .chart-panel{position:absolute;top:145px;height:38px;background:linear-gradient(180deg,#ffffff,#f1f4f7);border:.4px solid #e2e2e2}

  /* thank-you slide */
  .ty-photo{position:absolute;inset:0;background:linear-gradient(160deg,#e9622c 0%,#e45320 45%,#c8451a 100%)}
  .ty-word{left:0;right:0;top:48px;text-align:center;font-size:56px;color:#fff;letter-spacing:1px}
  .ty-band{left:0;top:125px;width:200px;height:31px;background:var(--navy)}
  .ty-text{left:100px;top:127px;font-family:"League Gothic",sans-serif;font-size:30px;color:#fff;letter-spacing:1px}
</style>
</head>
<body>
<main class="deck">

  <!-- 01 title -->
  <section class="slide s1">
    <div class="hero-photo" role="img" aria-label="Photograph of a lighthouse on a rocky coast at sunset"></div>
    <div class="hero-fade"></div>
    <div class="display wordmark">Quenvo</div>
    <div class="wordmark-rule"></div>
    <div class="abs display hero-get">Get Started <small>with the</small></div>
    <div class="abs hero-rule"></div>
    <div class="abs display hero-line" style="top:118px">Platform and then add</div>
    <div class="abs display hero-line" style="top:140px">The modules you need.</div>
    <div class="abs pill">The Engineering Operations Platform</div>
  </section>

  <!-- 02 text slide -->
  <section class="slide s2">
    <div class="abs display" style="left:0;right:0;top:14px;text-align:center;font-size:16px;color:var(--navy)">The <span style="color:var(--orange)">Connected</span></div>
    <div class="abs display" style="left:0;right:0;top:34px;text-align:center;font-size:11px;letter-spacing:2px;color:var(--navy)">Engineering Operations Platform</div>
    <div class="abs rule-navy" style="left:20px;right:20px;top:52px"></div>
    <div class="abs" style="left:20px;top:60px;width:153px">
      <div class="col-head on-light">Lorem ipsum dolor sit amet, consectetur adipiscing elit.</div>
      <div class="body col-text" style="margin-top:5px">
        <p>Lorem ipsum dolor sit amet, consectetur adipiscing elit. Mauris consectetur, quam at sagittis malesuada, ex justo luctus arcu, vitae tempor risus odio eu ipsum. Phasellus mauris tortor, lobortis sit amet ex eu, dictum venenatis libero.</p>
        <p>Nulla porta, arcu id euismod dictum, nunc elit molestie orci, eget molestie lacus urna id mi. Cras mollis, tellus eget ultricies volutpat, est augue sagittis ipsum, eget posuere nunc augue eget purus. Etiam interdum est nec interdum lobortis. Maecenas mauris augue, bibendum id lacus accumsan, aliquam interdum metus. Sed lobortis lorem vel magna blandit, eget consectetur lectus porttitor.</p>
        <p>Quisque dictum neque vitae urna suscipit, cursus euismod libero venenatis. Class aptent taciti sociosqu ad litora torquent per conubia nostra, per inceptos himenaeos.</p>
      </div>
    </div>
    <div class="abs" style="left:183px;top:60px;width:153px">
      <div class="col-head on-light">Lorem ipsum dolor sit amet, consectetur adipiscing elit.</div>
      <div class="body col-text" style="margin-top:5px">
        <p>Lorem ipsum dolor sit amet, consectetur adipiscing elit. Mauris consectetur, quam at sagittis malesuada, ex justo luctus arcu, vitae tempor risus odio eu ipsum. Phasellus mauris tortor, lobortis sit amet ex eu, dictum venenatis libero.</p>
        <p>Nulla porta, arcu id euismod dictum, nunc elit molestie orci, eget molestie lacus urna id mi. Cras mollis, tellus eget ultricies volutpat, est augue sagittis ipsum, eget posuere nunc augue eget purus. Etiam interdum est nec interdum lobortis. Maecenas mauris augue, bibendum id lacus accumsan, aliquam interdum metus. Sed lobortis lorem vel magna blandit, eget consectetur lectus porttitor.</p>
        <p>Quisque dictum neque vitae urna suscipit, cursus euismod libero venenatis. Class aptent taciti sociosqu ad litora torquent per conubia nostra, per inceptos himenaeos.</p>
      </div>
    </div>
    <div class="abs foot-num on-light">02</div>
    <div class="abs foot-url on-light">www.quenvomi.io</div>
    <div class="abs foot-rule"></div>
  </section>

  <!-- 03 feature slide -->
  <section class="slide s3">
    <div class="abs display" style="left:0;right:0;top:14px;text-align:center;font-size:19px;color:var(--orange)">Engineering Operations Platform</div>
    <div class="abs rule-orange" style="left:37px;right:37px;top:36px"></div>
    <div class="feature-art" style="left:38px" role="img" aria-label="Illustration of a workflow from planning to production"></div>
    <div class="feature-art" style="left:140px" role="img" aria-label="Illustration of a rising metrics chart"></div>
    <div class="feature-art" style="left:242px" role="img" aria-label="Illustration of a programming interface panel"></div>
    <div class="abs caption" style="left:38px;top:124px">Visibility from the backlog<br>to production (and beyond!)</div>
    <div class="abs body caption-sub" style="left:38px;top:142px;width:60px">Quenvo collects and presents data from the whole value stream of software engineering, with proper team attribution.</div>
    <div class="abs caption" style="left:140px;top:124px">100+ metrics and industry<br>benchmarks</div>
    <div class="abs body caption-sub" style="left:140px;top:142px;width:60px">Quenvo builds on recent delivery research to offer meaningful metrics, insights, and industry benchmarks.</div>
    <div class="abs caption" style="left:252px;top:124px">Configurable and<br>customizable APIs</div>
    <div class="abs body caption-sub" style="left:252px;top:142px;width:40px">Quenvo is an extensible API-based platform that allows you to send and inspect your data, and build your own reports.</div>
    <div class="abs foot-num on-dark">03</div>
    <div class="abs foot-url on-dark">www.quenvomi.io</div>
    <div class="abs foot-rule"></div>
  </section>

  <!-- 04 diagram slide -->
  <section class="slide s4">
    <div class="abs display" style="left:0;right:0;top:10px;text-align:center;font-size:20px;color:var(--navy)">Engineering Operations Platform</div>
    <div class="abs rule-navy" style="left:37px;right:37px;top:32px"></div>
    <div class="abs" role="img" aria-label="Architecture diagram of data sources, connectors, transformation, storage and external tools" style="left:78px;top:40px;width:204px;height:100px;background:linear-gradient(180deg,#eaf0f6,#dfe8f1);border:.5px solid #b9c8d8"></div>
    <div class="chart-panel" style="left:74px;width:46px" role="img" aria-label="Dashboard gauge panel"></div>
    <div class="chart-panel" style="left:123px;width:70px" role="img" aria-label="Dashboard line chart panel"></div>
    <div class="chart-panel" style="left:196px;width:88px" role="img" aria-label="Dashboard bar chart panel"></div>
    <div class="abs foot-num on-light">04</div>
    <div class="abs foot-url on-light">www.quenvomi.io</div>
    <div class="abs foot-rule"></div>
  </section>

  <!-- 05 dark text slide -->
  <section class="slide s5">
    <div class="abs display" style="left:0;right:0;top:19px;text-align:center;font-size:20px;color:var(--orange)">Engineering Operations Platform</div>
    <div class="abs rule-orange" style="left:40px;right:40px;top:43px"></div>
    <div class="abs" style="left:25px;top:53px;width:92px">
      <div class="col-head" style="color:var(--orange);font-size:12px">Lorem ipsum dolor sit amet</div>
      <div class="body col-text dark-text" style="margin-top:5px"><p>Lorem ipsum dolor sit amet, consectetur adipiscing elit. Mauris consectetur, quam at sagittis malesuada, ex justo luctus arcu, vitae tempor risus odio eu ipsum. Phasellus mauris tortor, lobortis sit amet ex eu.</p><p>Nulla porta, arcu id euismod dictum, nunc elit molestie orci, eget molestie lacus urna id mi. Cras mollis, tellus eget ultricies volutpat, est augue sagittis ipsum, eget posuere nunc augue eget purus.</p><p>Aliquam interdum metus. Sed lobortis lorem vel magna blandit, eget consectetur lectus porttitor.</p><p>Et laoreet purus, ut tincidunt neque dignissim et.</p></div>
    </div>
    <div class="abs" style="left:132px;top:53px;width:92px">
      <div class="col-head" style="color:var(--orange);font-size:12px">Lorem ipsum dolor sit amet</div>
      <div class="body col-text dark-text" style="margin-top:5px"><p>Lorem ipsum dolor sit amet, consectetur adipiscing elit. Mauris consectetur, quam at sagittis malesuada, ex justo luctus arcu, vitae tempor risus odio eu ipsum. Phasellus mauris tortor, lobortis sit amet ex eu.</p><p>Nulla porta, arcu id euismod dictum, nunc elit molestie orci, eget molestie lacus urna id mi. Cras mollis, tellus eget ultricies volutpat, est augue sagittis ipsum, eget posuere nunc augue eget purus.</p><p>Aliquam interdum metus. Sed lobortis lorem vel magna blandit, eget consectetur lectus porttitor.</p><p>Et laoreet purus, ut tincidunt neque dignissim et.</p></div>
    </div>
    <div class="abs" style="left:239px;top:53px;width:92px">
      <div class="col-head" style="color:var(--orange);font-size:12px">Lorem ipsum dolor sit amet</div>
      <div class="body col-text dark-text" style="margin-top:5px"><p>Lorem ipsum dolor sit amet, consectetur adipiscing elit. Mauris consectetur, quam at sagittis malesuada, ex justo luctus arcu, vitae tempor risus odio eu ipsum. Phasellus mauris tortor, lobortis sit amet ex eu.</p><p>Nulla porta, arcu id euismod dictum, nunc elit molestie orci, eget molestie lacus urna id mi. Cras mollis, tellus eget ultricies volutpat, est augue sagittis ipsum, eget posuere nunc augue eget purus.</p><p>Aliquam interdum metus. Sed lobortis lorem vel magna blandit, eget consectetur lectus porttitor.</p><p>Et laoreet purus, ut tincidunt neque dignissim et.</p></div>
    </div>
    <div class="abs foot-num on-dark">05</div>
    <div class="abs foot-url on-dark">www.quenvomi.io</div>
    <div class="abs foot-rule"></div>
  </section>

  <!-- 06 thank you -->
  <section class="slide s6">
    <div class="ty-photo" role="img" aria-label="Orange-toned photograph of a lighthouse on a rocky shore"></div>
    <div class="abs display ty-word">Quenvo</div>
    <div class="abs ty-band"></div>
    <div class="abs ty-text">THANK YOU</div>
  </section>

</main>
</body>
</html>
```